7 page website for Dog Training Business

we are seeking a website design that should be 7 pages for a Las Vegas Dog training business. the site will have a heavy focus on video, and social media. Ideas design can be borrowed from http://bramblevox.net
attached is a copy of the logo and business card mock up. Content is currently being written and will be posted shortly

Training

```html
<!DOCTYPE html>
<html lang="en">
<head>
<meta charset="utf-8">
<title>KORVO Dog Training – Las Vegas</title>
<link rel="stylesheet" href="https://fonts.googleapis.com/css2?family=Abel&family=Open+Sans:wght@400;600;700;800&display=swap">
<style>
:root{
  --tan:#c3844f;
  --forest:#3c5a3e;
  --lime:#a9c94b;
  --lime-dark:#8fb03a;
  --nav:#4f7243;
  --brown:#744526;
  --brown-mid:#8a5632;
  --ink:#333;
  --white:#fff;
  --col-a:#f7efed;
  --col-b:#eef0f7;
  --col-c:#f3f6e4;
}
*{box-sizing:border-box;margin:0;padding:0}
html,body{width:934px;height:1200px;overflow:hidden}
body{position:relative;background:linear-gradient(var(--tan) 0 375px,var(--forest) 375px);font-family:"Open Sans",sans-serif;color:var(--ink)}
.abs{position:absolute}

/* top bar */
.topbar{left:237px;top:0;width:460px;height:16px;border-bottom:1px solid rgba(80,50,30,.45);display:flex;justify-content:flex-end;align-items:center;gap:6px;font-size:7px;color:var(--white)}
.topbar .item{display:flex;align-items:center;gap:3px}
.icon-dot{width:8px;height:8px;border-radius:50%;background:#2d2d2d;display:inline-block}
.social{width:13px;height:13px;background:#3b4f86;display:inline-block}
.social.alt{background:#b02a22}

.brand{left:238px;top:30px;display:flex;align-items:center;gap:6px}
.brand .mark{width:56px;height:56px;border-radius:50%;background:var(--lime)}
.brand .name{font-family:"Open Sans",sans-serif;font-weight:800;font-size:11px;color:var(--white);line-height:1.15;width:70px}

.quote{left:535px;top:38px;width:162px;padding:0 14px;text-align:center;font-size:5.5px;color:var(--white);line-height:1.3}
.quote b{display:block;font-size:6px}
.quote .mk{position:absolute;top:-2px;font-size:20px;font-weight:800;color:var(--lime);line-height:1}
.tag{background:var(--lime);color:#2f4a22;font-size:5.5px;font-weight:700;text-transform:uppercase;display:flex;align-items:center;justify-content:center;clip-path:polygon(0 0,90% 0,100% 50%,90% 100%,0 100%)}

.nav{left:237px;top:101px;width:460px;height:20px;background:var(--nav);border-radius:2px;display:flex;font-family:"Abel",sans-serif;font-size:9px;color:var(--white);box-shadow:0 1px 2px rgba(0,0,0,.3)}
.nav a{color:inherit;text-decoration:none;display:flex;align-items:center;justify-content:center;height:100%}
.nav a.active{background:var(--brown);color:var(--lime);border-radius:2px 0 0 2px}

.hero-title{left:237px;top:143px;font-family:"Abel",sans-serif;font-weight:400;font-size:20px;color:#3e5a34;letter-spacing:.3px}
.hero-sub{left:237px;top:164px;font-family:"Abel",sans-serif;font-size:12px;color:#b7d451}
.hero-rule{left:237px;top:185px;width:220px;height:1px;background:var(--brown)}
.hero-text{left:237px;top:192px;width:222px;font-size:6px;color:var(--white);line-height:1.5}
.thumb{top:217px;width:65px;height:42px;border:2px solid var(--white);background:linear-gradient(135deg,#7a9a4a,#6b5a3e)}
.play{position:absolute;left:50%;top:50%;transform:translate(-50%,-50%);width:12px;height:12px;border-radius:50%;background:rgba(0,0,0,.55)}
.play::after{content:"";position:absolute;left:4.5px;top:3px;border-left:5px solid #fff;border-top:3px solid transparent;border-bottom:3px solid transparent}
.link-more{left:320px;top:272px;font-size:7.5px;font-weight:700;color:var(--lime)}
.btn-outline{left:385px;top:270px;width:70px;height:15px;border:1px solid #f0d4b8;font-size:7px;font-weight:700;color:var(--lime);display:flex;align-items:center;justify-content:center}
.video{left:482px;top:145px;width:211px;height:140px;border:3px solid var(--white);background:linear-gradient(#4c6e36 0 45%,#6f9a45 45%);box-shadow:0 1px 4px rgba(0,0,0,.3)}
.video .play{width:30px;height:30px}
.video .play::after{left:12px;top:8px;border-left:9px solid #fff;border-top:7px solid transparent;border-bottom:7px solid transparent}
.arrow-btn{top:190px;width:19px;height:19px;background:rgba(255,255,255,.35);border-radius:2px}

/* main panel */
.panel{left:233px;top:305px;width:468px;height:733px;background:var(--white);box-shadow:0 0 12px rgba(0,0,0,.25)}
.trainer-photo{left:243px;top:323px;width:95px;height:113px;background:linear-gradient(#f4f4f4,#d9d4cc)}
.blob{left:330px;top:330px;width:145px;height:108px;border-radius:50px 60px 55px 40px;background:#d9b995}
.big{font-family:"Open Sans",sans-serif;font-weight:800;line-height:.95;text-align:center;width:130px;left:336px}
.meet{left:477px;top:324px;font-family:"Abel",sans-serif;font-weight:400;font-size:14px;color:#3b3b3b}
.meet-rule{left:477px;top:343px;width:220px;height:1px;background:var(--brown)}
.portrait{top:353px;width:70px;height:70px;border-radius:50%;background:radial-gradient(#a7b98a,#5b7a3c)}
.pname{top:431px;width:70px;text-align:center;font-size:6px;font-weight:700;color:var(--brown)}
.about{left:237px;top:476px;width:232px;font-size:6px;line-height:1.45}
.badge{top:470px;width:56px;height:56px;border-radius:50%}

.col{top:565px;width:153px;height:320px;padding:0 3px;overflow:hidden}
.col .media{position:relative;height:76px;margin:2px 0 8px}
.col .media h3{position:absolute;left:3px;top:2px;color:var(--white);font-size:13.5px;font-weight:700;line-height:1.2;text-transform:uppercase;text-shadow:0 1px 2px rgba(0,0,0,.5)}
.col .media .tag{position:absolute;right:0;bottom:3px;width:65px;height:11px}
.service{margin-bottom:6px}
.service h4{font-family:"Abel",sans-serif;font-weight:400;font-size:10.5px;line-height:13px;color:var(--brown-mid);display:flex;align-items:center;gap:4px;margin-bottom:2px}
.paw{width:14px;height:11px;display:inline-block}
.service p{font-size:6px;line-height:9px}

.hours-title{left:237px;top:930px;font-family:"Abel",sans-serif;font-weight:400;font-size:11px;color:var(--brown-mid)}
.hours{left:237px;top:948px;font-size:6px;border-collapse:collapse}
.hours td{height:11.7px;padding:0}
.hours td:first-child{width:42px}
.map{left:336px;top:926px;width:205px;height:87px;background:linear-gradient(135deg,#e8e4da,#d8d5cc)}
.fb{left:549px;top:903px;width:148px;height:111px;border:1px solid #c5c9d6;font-size:5px;color:#555}
.fb .hd{height:10px;border-bottom:1px solid #c5c9d6;background:#eef0f5;padding:2px 3px;font-weight:700}
.fb .grid{position:absolute;left:4px;top:48px;display:grid;grid-template-columns:repeat(6,18px);gap:2px}
.fb .grid span{height:17px;background:#6a6a78}

.fnav{top:1048px;font-family:"Abel",sans-serif;font-size:7.5px;color:var(--white)}
.frule{left:237px;top:1064px;width:460px;height:1px;background:rgba(255,255,255,.6)}
.news{left:237px;top:1076px;font-family:"Abel",sans-serif;font-weight:400;font-size:10px;color:var(--lime)}
.field{left:237px;width:117px;height:14px;background:var(--white);font-size:6px;color:#666;padding:3px 4px}
.contact-line{left:237px;top:1156px;display:flex;gap:6px;align-items:center;font-size:7px;color:var(--white)}
.contact-line .item{display:flex;gap:3px;align-items:center}
.footer-mark{left:640px;top:1079px;width:58px;height:58px;border-radius:50%;background:var(--lime)}
.footer-copy{left:620px;top:1142px;width:78px;text-align:right;font-size:5.5px;color:var(--white);line-height:1.6}
</style>
</head>
<body>

<header>
  <div class="abs topbar">
    <span class="item"><i class="icon-dot"></i>(702) 555 0147</span>
    <span class="item"><i class="icon-dot"></i>hello@korvotraining.com</span>
    <i class="social"></i><i class="social alt"></i>
  </div>

  <div class="abs brand"><span class="mark"></span><span class="name">KORVO Dog Training</span></div>

  <div class="abs quote">
    <span class="mk" style="left:0">“</span><span class="mk" style="right:0">”</span>
    Aenean et odio semper, maximus turpis quis, pellentesque turpis. Cras eu dictum felis. Lorem ipsum dolor sit amet.
    <b>JHON DOE</b>
  </div>
  <div class="abs tag" style="left:632px;top:69px;width:66px;height:14px">All testimonials</div>

  <nav class="abs nav">
    <a class="active" href="#" style="width:50px">HOME</a>
    <a href="#" style="width:67px">SERVICES</a>
    <a href="#" style="width:90px">PHOTOS / VIDEOS</a>
    <a href="#" style="width:77px">TESTIMONIALS</a>
    <a href="#" style="width:56px">STORE</a>
    <a href="#" style="width:60px">ABOUT</a>
    <a href="#" style="width:60px">CONTACT</a>
  </nav>
</header>

<section class="hero">
  <div class="abs arrow-btn" style="left:199px"><svg width="19" height="19"><path d="M11 5 L7 9.5 L11 14" stroke="#fff" stroke-width="2" fill="none"/></svg></div>
  <div class="abs arrow-btn" style="left:715px"><svg width="19" height="19"><path d="M8 5 L12 9.5 L8 14" stroke="#fff" stroke-width="2" fill="none"/></svg></div>
  <h1 class="abs hero-title">DOG &amp; PUPPY TRAINING</h1>
  <p class="abs hero-sub">In Las Vegas</p>
  <div class="abs hero-rule"></div>
  <p class="abs hero-text">Lorem ipsum dolor sit amet, consectetur adipiscing elit. Nam in pharetra eros, semper ultricies est. Sed ac condimentum risus.</p>
  <div class="abs thumb" style="left:237px" role="img" aria-label="Video thumbnail: hands rewarding a dog"><span class="play"></span></div>
  <div class="abs thumb" style="left:314px" role="img" aria-label="Video thumbnail: trainer with a dog"><span class="play"></span></div>
  <div class="abs thumb" style="left:390px" role="img" aria-label="Video thumbnail: group of dogs"><span class="play"></span></div>
  <span class="abs link-more">LEARN MORE ›</span>
  <span class="abs btn-outline">OUR SERVICES ›</span>
  <div class="abs video" role="img" aria-label="Video: dog sitting up to a trainer's hand signal on a lawn"><span class="play"></span></div>
</section>

<main>
  <div class="abs panel"></div>

  <div class="abs trainer-photo" role="img" aria-label="Trainer giving a command to a seated shepherd dog"></div>
  <div class="abs blob" role="img" aria-label="Soft paw-shaped backdrop"></div>
  <div class="abs big" style="top:334px;font-size:44px;color:var(--brown)">OVER</div>
  <div class="abs big" style="top:375px;font-size:17px;color:var(--lime)">1250 DOGS</div>
  <div class="abs big" style="top:393px;font-size:15px;color:#3e5a34">AND OWNERS</div>
  <div class="abs big" style="top:407px;font-size:33px;color:var(--brown)">HELPED</div>

  <h2 class="abs meet">Meet our trainers</h2>
  <div class="abs tag" style="left:632px;top:326px;width:65px;height:14px">All trainers</div>
  <div class="abs meet-rule"></div>
  <svg class="abs" style="left:479px;top:384px" width="12" height="18"><path d="M10 1 L2 9 L10 17" stroke="var(--lime)" stroke-width="3" fill="none"/></svg>
  <svg class="abs" style="left:684px;top:384px" width="12" height="18"><path d="M2 1 L10 9 L2 17" stroke="var(--lime)" stroke-width="3" fill="none"/></svg>
  <div class="abs portrait" style="left:506px" role="img" aria-label="Trainer portrait with dogs"></div>
  <div class="abs portrait" style="left:600px" role="img" aria-label="Trainer portrait with dogs"></div>
  <p class="abs pname" style="left:506px">John Doe</p>
  <p class="abs pname" style="left:600px">Jane Doe</p>

  <p class="abs about"><b>KORVO Dog Training</b> dolor sit amet, consectetur adipiscing elit. Nam in pharetra eros, semper ultricies est. Sed ac condimentum risus. Maecenas dictum fermentum ex, quis sodales ex condimentum sit amet. Sed tincidunt nulla sed facilisis facilisis. Praesent imperdiet posuere eros id pharetra. <i>Ut nec nisi nibh.</i> Phasellus eu molestie elit. Nunc non tincidunt neque, sit amet finibus tellus. Nullam id justo et libero cursus tincidunt sed a risus. Curabitur vitae fringilla nunc. <i>Quisque risus mi, efficitur eget porta vel, sollicitudin vel neque.</i></p>
  <div class="abs badge" style="left:477px;background:#f1c27a"></div>
  <div class="abs badge" style="left:556px;background:#2f56a4"></div>
  <div class="abs badge" style="left:640px;background:#f2d23a"></div>

  <section class="abs col" style="left:235px;background:var(--col-a)">
    <div class="media" role="img" aria-label="Photo: trainer with dog at home" style="background:linear-gradient(135deg,#3f6a2a,#8a7a4a)"><h3>In-Home<br>Training</h3><span class="tag">Video gallery</span></div>
    <div class="service"><h4><svg class="paw" viewBox="0 0 14 11"><g fill="var(--lime)"><ellipse cx="7" cy="8" rx="3.5" ry="2.8"/><circle cx="2" cy="4.5" r="1.5"/><circle cx="5" cy="2" r="1.5"/><circle cx="9" cy="2" r="1.5"/><circle cx="12" cy="4.5" r="1.5"/></g></svg>One-on-One In-Home Sessions</h4><p>Sed ac condimentum risus. Maecenas dictum fermentum ex, quis sodales ex condimentum sit amet. Sed tincidunt nulla sed facilisis facilisis. Praesent imperdiet posuere eros id pharetra</p></div>
    <div class="service"><h4><svg class="paw" viewBox="0 0 14 11"><g fill="var(--lime)"><ellipse cx="7" cy="8" rx="3.5" ry="2.8"/><circle cx="2" cy="4.5" r="1.5"/><circle cx="5" cy="2" r="1.5"/><circle cx="9" cy="2" r="1.5"/><circle cx="12" cy="4.5" r="1.5"/></g></svg>Off-Leash Basics Program</h4><p>Sed ac condimentum risus. Maecenas dictum fermentum ex, quis sodales ex condimentum sit amet. Sed tincidunt nulla sed facilisis facilisis. Praesent imperdiet posuere eros id pharetra</p></div>
    <div class="service"><h4><svg class="paw" viewBox="0 0 14 11"><g fill="var(--lime)"><ellipse cx="7" cy="8" rx="3.5" ry="2.8"/><circle cx="2" cy="4.5" r="1.5"/><circle cx="5" cy="2" r="1.5"/><circle cx="9" cy="2" r="1.5"/><circle cx="12" cy="4.5" r="1.5"/></g></svg>Mini-Sessions</h4><p>Sed ac condimentum risus. Maecenas dictum fermentum ex, quis sodales ex condimentum sit amet. Sed tincidunt nulla sed facilisis facilisis. Praesent imperdiet posuere eros id pharetra</p></div>
    <div class="service"><h4><svg class="paw" viewBox="0 0 14 11"><g fill="var(--lime)"><ellipse cx="7" cy="8" rx="3.5" ry="2.8"/><circle cx="2" cy="4.5" r="1.5"/><circle cx="5" cy="2" r="1.5"/><circle cx="9" cy="2" r="1.5"/><circle cx="12" cy="4.5" r="1.5"/></g></svg>'The Walk Doctor' Program</h4><p>Sed ac condimentum risus. Maecenas dictum fermentum ex, quis sodales ex condimentum sit amet. Sed tincidunt nulla sed facilisis facilisis. Praesent imperdiet posuere eros id pharetra</p></div>
  </section>

  <section class="abs col" style="left:390px;background:var(--col-b)">
    <div class="media" role="img" aria-label="Photo: dogs training on grass" style="background:linear-gradient(135deg,#4e6a3a,#8aa86a)"><h3>Board-and-Train<br>Packages</h3><span class="tag">Video gallery</span></div>
    <div class="service"><h4><svg class="paw" viewBox="0 0 14 11"><g fill="var(--lime)"><ellipse cx="7" cy="8" rx="3.5" ry="2.8"/><circle cx="2" cy="4.5" r="1.5"/><circle cx="5" cy="2" r="1.5"/><circle cx="9" cy="2" r="1.5"/><circle cx="12" cy="4.5" r="1.5"/></g></svg>One-on-One In-Home Sessions</h4><p>Sed ac condimentum risus. Maecenas dictum fermentum ex, quis sodales ex condimentum sit amet. Sed tincidunt nulla sed facilisis facilisis. Praesent imperdiet posuere eros id pharetra</p></div>
    <div class="service"><h4><svg class="paw" viewBox="0 0 14 11"><g fill="var(--lime)"><ellipse cx="7" cy="8" rx="3.5" ry="2.8"/><circle cx="2" cy="4.5" r="1.5"/><circle cx="5" cy="2" r="1.5"/><circle cx="9" cy="2" r="1.5"/><circle cx="12" cy="4.5" r="1.5"/></g></svg>Off-Leash Basics Program</h4><p>Sed ac condimentum risus. Maecenas dictum fermentum ex, quis sodales ex condimentum sit amet. Sed tincidunt nulla sed facilisis facilisis. Praesent imperdiet posuere eros id pharetra</p></div>
    <div class="service"><h4><svg class="paw" viewBox="0 0 14 11"><g fill="var(--lime)"><ellipse cx="7" cy="8" rx="3.5" ry="2.8"/><circle cx="2" cy="4.5" r="1.5"/><circle cx="5" cy="2" r="1.5"/><circle cx="9" cy="2" r="1.5"/><circle cx="12" cy="4.5" r="1.5"/></g></svg>Mini-Sessions</h4><p>Sed ac condimentum risus. Maecenas dictum fermentum ex, quis sodales ex condimentum sit amet. Sed tincidunt nulla sed facilisis facilisis. Praesent imperdiet posuere eros id pharetra</p></div>
    <div class="service"><h4><svg class="paw" viewBox="0 0 14 11"><g fill="var(--lime)"><ellipse cx="7" cy="8" rx="3.5" ry="2.8"/><circle cx="2" cy="4.5" r="1.5"/><circle cx="5" cy="2" r="1.5"/><circle cx="9" cy="2" r="1.5"/><circle cx="12" cy="4.5" r="1.5"/></g></svg>'The Walk Doctor' Program</h4><p>Sed ac condimentum risus. Maecenas dictum fermentum ex, quis sodales ex condimentum sit amet. Sed tincidunt nulla sed facilisis facilisis. Praesent imperdiet posuere eros id pharetra</p></div>
  </section>

  <section class="abs col" style="left:545px;background:var(--col-c)">
    <div class="media" role="img" aria-label="Photo: dog beside a telephone" style="background:linear-gradient(135deg,#2d4a6e,#b08a5a)"><h3>Phone<br>Consultation<br>Training</h3><span class="tag">Video gallery</span></div>
    <div class="service"><h4><svg class="paw" viewBox="0 0 14 11"><g fill="var(--lime)"><ellipse cx="7" cy="8" rx="3.5" ry="2.8"/><circle cx="2" cy="4.5" r="1.5"/><circle cx="5" cy="2" r="1.5"/><circle cx="9" cy="2" r="1.5"/><circle cx="12" cy="4.5" r="1.5"/></g></svg>One-on-One In-Home Sessions</h4><p>Sed ac condimentum risus. Maecenas dictum fermentum ex, quis sodales ex condimentum sit amet. Sed tincidunt nulla sed facilisis facilisis. Praesent imperdiet posuere eros id pharetra</p></div>
    <div class="service"><h4><svg class="paw" viewBox="0 0 14 11"><g fill="var(--lime)"><ellipse cx="7" cy="8" rx="3.5" ry="2.8"/><circle cx="2" cy="4.5" r="1.5"/><circle cx="5" cy="2" r="1.5"/><circle cx="9" cy="2" r="1.5"/><circle cx="12" cy="4.5" r="1.5"/></g></svg>Off-Leash Basics Program</h4><p>Sed ac condimentum risus. Maecenas dictum fermentum ex, quis sodales ex condimentum sit amet. Sed tincidunt nulla sed facilisis facilisis. Praesent imperdiet posuere eros id pharetra</p></div>
    <div class="service"><h4><svg class="paw" viewBox="0 0 14 11"><g fill="var(--lime)"><ellipse cx="7" cy="8" rx="3.5" ry="2.8"/><circle cx="2" cy="4.5" r="1.5"/><circle cx="5" cy="2" r="1.5"/><circle cx="9" cy="2" r="1.5"/><circle cx="12" cy="4.5" r="1.5"/></g></svg>Mini-Sessions</h4><p>Sed ac condimentum risus. Maecenas dictum fermentum ex, quis sodales ex condimentum sit amet. Sed tincidunt nulla sed facilisis facilisis. Praesent imperdiet posuere eros id pharetra</p></div>
    <div class="service"><h4><svg class="paw" viewBox="0 0 14 11"><g fill="var(--lime)"><ellipse cx="7" cy="8" rx="3.5" ry="2.8"/><circle cx="2" cy="4.5" r="1.5"/><circle cx="5" cy="2" r="1.5"/><circle cx="9" cy="2" r="1.5"/><circle cx="12" cy="4.5" r="1.5"/></g></svg>'The Walk Doctor' Program</h4><p>Sed ac condimentum risus. Maecenas dictum fermentum ex, quis sodales ex condimentum sit amet. Sed tincidunt nulla sed facilisis facilisis. Praesent imperdiet posuere eros id pharetra</p></div>
  </section>

  <h3 class="abs hours-title">Business Hours</h3>
  <table class="abs hours">
    <tr><td>Monday</td><td>9:00 am - 8:00 pm</td></tr>
    <tr><td>Tuesday</td><td>9:00 am - 8:00 pm</td></tr>
    <tr><td>Wednesday</td><td>9:00 am - 8:00 pm</td></tr>
    <tr><td>Thursday</td><td>9:00 am - 8:00 pm</td></tr>
    <tr><td>Friday</td><td>9:00 am - 8:00 pm</td></tr>
    <tr><td>Saturday</td><td>10:00 am - 12:00 pm</td></tr>
  </table>
  <div class="abs map" role="img" aria-label="Street map of the training location"></div>
  <div class="abs fb">
    <div class="hd">Find us on our page</div>
    <div style="position:absolute;left:4px;top:14px;width:18px;height:18px;background:#6a6a78"></div>
    <div style="position:absolute;left:26px;top:15px;color:#3b5998;font-weight:700">Silverline Pup Academy</div>
    <div style="position:absolute;left:26px;top:23px;width:28px;height:7px;background:#4b67a1"></div>
    <div style="position:absolute;left:4px;top:39px">444 people like Silverline Pup Academy</div>
    <div class="grid"><span></span><span></span><span></span><span></span><span></span><span></span><span></span><span></span><span></span><span></span><span></span><span></span></div>
    <div style="position:absolute;left:4px;top:95px">Social page plugin</div>
  </div>
</main>

<footer>
  <span class="abs fnav" style="left:237px">HOME</span>
  <span class="abs fnav" style="left:281px">SERVICES</span>
  <span class="abs fnav" style="left:335px">PHOTOS / VIDEOS</span>
  <span class="abs fnav" style="left:409px">TESTIMONIALS</span>
  <span class="abs fnav" style="left:476px">STORE</span>
  <span class="abs fnav" style="left:520px">ABOUT</span>
  <span class="abs fnav" style="left:565px">CONTACT</span>
  <i class="abs social" style="left:670px;top:1046px"></i>
  <i class="abs social alt" style="left:687px;top:1046px"></i>
  <div class="abs frule"></div>
  <h3 class="abs news">Join our newsletter</h3>
  <div class="abs field" style="top:1092px">Name</div>
  <div class="abs field" style="top:1113px">Email</div>
  <div class="abs tag" style="left:289px;top:1135px;width:65px;height:13px">Submit</div>
  <div class="abs contact-line">
    <span class="item"><i class="icon-dot" style="background:#fff"></i>(702) 555 0147</span>
    <span class="item"><i class="icon-dot" style="background:#fff"></i>hello@korvotraining.com</span>
  </div>
  <div class="abs footer-mark"></div>
  <p class="abs footer-copy">KORVO DOG TRAINING<br>All rights reserved 2015</p>
</footer>

</body>
</html>
```